Business card for Real Estate Company located in Coastal area of spain

Want a business card design. Simple, professional, horizontal layout. will be 2 sided. Name of company (logo big on front). Name of agent, phone and email address. Back side will be list of general services we provide. Would like to see 2 separate concepts using the 2 separate logo treatments. One using Rich dark, bright blue as the stock color, and the other using White as the stock color.
Logo files uploaded (2 different versions) Domain (bayridgedwell48.com) Moraira-Calpe-Altea-Javea-Denia-Marina Alta Area (perhaps across the bottom of the front of card0 Petra Linde Licensed Estate Agent / Partner Petra@bayridgedwell48.com +34.681.72.40.96 Back of card should list services offered

Real Estate Sales and Investments Real Estate Rental Management Kitchen, Bathroom Reformations Complete Home Reformation Services Window and Door Replacement Landscape and Garden Management Pool and Jacuzzi Service

Target Market(s)

Real estate and construction

Industry/Entity Type

Real Estate

Contact Information for Business Card

Logo files uploaded (2 different versions) Domain (bayridgedwell48.com) Moraira-Calpe-Altea-Javea-Denia-Marina Alta Area (perhaps across the bottom of the front of card0 Petra Linde Licensed Estate Agent / Partner Petra@bayridgedwell48.com +34.681.72.40.96

Colors

Designer to choose colors to be used in the design.

Requirements
Must have
• progressive look professional
Nice to have
• Front big logo, Agent details. Back, list of services included in project description
Should not have
• Gloss finish for card

```html
<!DOCTYPE html>
<html lang="en">
<head>
<meta charset="utf-8">
<title>bayridgedwell48.com — Business Card</title>
<link rel="stylesheet" href="https://fonts.googleapis.com/css2?family=Open+Sans:wght@400;700&family=Poppins:wght@700&family=Bebas+Neue&family=Montserrat:wght@400;500&display=swap">
<style>
  :root {
    --page: #e4e4e6;
    --stock: #f1f1f3;
    --navy: #0d2f7a;
    --brand: #22409a;
    --violet: #5b3fd6;
    --ink: #1c1c28;
    --grey: #4a4a52;
    --rule: #7b8fb8;
  }
  * { box-sizing: border-box; margin: 0; padding: 0; }
  html, body { width: 1200px; height: 1157px; overflow: hidden; }
  body { background: var(--page); position: relative; font-family: "Montserrat", sans-serif; }

  .card {
    position: absolute; left: 300px; width: 600px; height: 344px;
    background: var(--stock); border-radius: 18px; overflow: hidden;
  }
  .card--front { top: 214px; }
  .card--back { top: 594px; }
  .card__art { position: absolute; inset: 0; width: 600px; height: 344px; }

  .brand-name {
    position: absolute; left: 52px; top: 22px; width: 505px; text-align: center;
    font-family: "Open Sans", sans-serif; font-weight: 400; font-size: 47px;
    color: var(--brand); letter-spacing: -0.5px; line-height: 1;
  }
  .brand-tagline {
    position: absolute; left: 52px; top: 78px; width: 505px; text-align: center;
    font-family: "Poppins", sans-serif; font-weight: 700; font-size: 11.5px;
    letter-spacing: 0.42em; color: var(--navy);
  }
  .agent-name {
    position: absolute; left: 38px; top: 142px;
    font-family: "Open Sans", sans-serif; font-size: 44px; line-height: 1; letter-spacing: -1px;
  }
  .agent-name__first { font-weight: 700; color: var(--navy); }
  .agent-name__last { font-weight: 400; color: var(--grey); }
  .agent-title {
    position: absolute; left: 39px; top: 202px;
    font-family: "Bebas Neue", sans-serif; font-size: 16px; letter-spacing: 0.2em; color: var(--ink);
  }
  .agent-rule { position: absolute; left: 39px; top: 231px; width: 62px; height: 2px; background: var(--navy); }
  .contact { position: absolute; left: 37px; display: flex; align-items: center; gap: 12px;
    font-size: 11.5px; color: var(--ink); }
  .contact--email { top: 249px; }
  .contact--phone { top: 276px; }
  .contact__icon { width: 23px; height: 23px; flex: none; }

  .services-icons { position: absolute; left: 0; top: 30px; width: 600px; height: 50px; }
  .service-icon {
    position: absolute; top: 2px; width: 46px; height: 46px; border-radius: 6px;
    background: linear-gradient(135deg, var(--navy), var(--violet)); opacity: 0.85;
  }
  .service-divider { position: absolute; top: 4px; width: 2px; height: 43px; background: var(--navy); }

  .services { list-style: none; position: absolute; left: 45px; top: 112px; width: 290px; }
  .services__item {
    font-size: 13.5px; font-weight: 500; color: var(--ink); line-height: 1.25;
    padding-bottom: 10px; margin-bottom: 12px; position: relative;
  }
  .services__item::after {
    content: ""; position: absolute; left: 0; bottom: 0; width: 62px; height: 1px; background: var(--rule);
  }
  .services__item:last-child::after { display: none; }
  .services__item:nth-child(4) { margin-bottom: 8px; }

  .brand-mini {
    position: absolute; left: 24px; top: 314px; width: 122px; text-align: center;
  }
  .brand-mini__name { font-family: "Open Sans", sans-serif; font-size: 12.5px; color: var(--brand); line-height: 1; }
  .brand-mini__tag { font-family: "Poppins", sans-serif; font-weight: 700; font-size: 3.6px;
    letter-spacing: 0.18em; color: var(--navy); margin-top: 2px; }
</style>
</head>
<body>

<section class="card card--front" aria-label="Card front">
  <svg class="card__art" viewBox="0 0 600 344" aria-hidden="false">
    <defs>
      <linearGradient id="seaFront" x1="0" y1="0" x2="0" y2="1">
        <stop offset="0" stop-color="#7a52f0"/>
        <stop offset="0.45" stop-color="#4a2fd0"/>
        <stop offset="1" stop-color="#241a7a"/>
      </linearGradient>
      <linearGradient id="cornerBlue" x1="0" y1="1" x2="1" y2="0">
        <stop offset="0" stop-color="#0d2f7a"/>
        <stop offset="1" stop-color="#2a4fc4"/>
      </linearGradient>
    </defs>
    <path d="M0,64 C14,30 42,8 77,0 L0,0 Z" fill="url(#cornerBlue)"/>
    <path role="img" aria-label="Photo of the rocky Mediterranean coastline at dusk" d="M156,344 C330,292 530,200 600,14 L600,344 Z" fill="url(#seaFront)"/>
    <path d="M205,344 C330,300 430,240 494,172 C445,232 350,298 226,344 Z" fill="var(--stock)"/>
  </svg>

  <div class="brand-name">bayridgedwell48.com</div>
  <div class="brand-tagline">REAL ESTATE-REFORMS-HOME SERVICES</div>

  <h1 class="agent-name"><span class="agent-name__first">PETRA</span> <span class="agent-name__last">LINDE</span></h1>
  <div class="agent-title">Licensed Estate Agent / Partner</div>
  <div class="agent-rule"></div>

  <div class="contact contact--email">
    <svg class="contact__icon" viewBox="0 0 24 24" aria-hidden="true">
      <polygon points="12,1 22,6.5 22,17.5 12,23 2,17.5 2,6.5" fill="var(--navy)"/>
      <rect x="6.5" y="8" width="11" height="8" fill="none" stroke="#fff" stroke-width="1.3"/>
      <path d="M6.5,8 L12,12.5 L17.5,8" fill="none" stroke="#fff" stroke-width="1.3"/>
    </svg>
    <span>Petra@bayridgedwell48.com</span>
  </div>
  <div class="contact contact--phone">
    <svg class="contact__icon" viewBox="0 0 24 24" aria-hidden="true">
      <polygon points="12,1 22,6.5 22,17.5 12,23 2,17.5 2,6.5" fill="var(--navy)"/>
      <path d="M8.5,7 L10.5,7 L11.3,9.6 L10,10.6 C10.7,12.2 11.8,13.3 13.4,14 L14.4,12.7 L17,13.5 L17,15.5 C12,16 8,12 8.5,7 Z" fill="#fff"/>
    </svg>
    <span>+34.681.72.40.96</span>
  </div>
</section>

<section class="card card--back" aria-label="Card back">
  <svg class="card__art" viewBox="0 0 600 344">
    <defs>
      <linearGradient id="villaBack" x1="0" y1="0" x2="0" y2="1">
        <stop offset="0" stop-color="#3a2bb8"/>
        <stop offset="0.5" stop-color="#5a44c8"/>
        <stop offset="1" stop-color="#1e1660"/>
      </linearGradient>
      <linearGradient id="cornerBlueB" x1="0" y1="1" x2="1" y2="0">
        <stop offset="0" stop-color="#0d2f7a"/>
        <stop offset="1" stop-color="#2a4fc4"/>
      </linearGradient>
    </defs>
    <path d="M0,64 C14,30 42,8 80,0 L0,0 Z" fill="url(#cornerBlueB)"/>
    <path role="img" aria-label="Photo of a white coastal villa with balustraded terraces" d="M160,344 C340,292 540,200 600,16 L600,344 Z" fill="url(#villaBack)"/>
    <path d="M210,344 C335,300 435,240 497,172 C448,232 355,298 232,344 Z" fill="var(--stock)"/>
  </svg>

  <div class="services-icons">
    <div class="service-icon" style="left:88px" role="img" aria-label="Icon: building and house held in a hand"></div>
    <div class="service-divider" style="left:159px"></div>
    <div class="service-icon" style="left:185px" role="img" aria-label="Icon: agent managing property, money and search"></div>
    <div class="service-divider" style="left:257px"></div>
    <div class="service-icon" style="left:275px" role="img" aria-label="Icon: house with repair tools"></div>
    <div class="service-divider" style="left:345px"></div>
    <div class="service-icon" style="left:372px" role="img" aria-label="Icon: trees, plants and garden fence"></div>
    <div class="service-divider" style="left:442px"></div>
    <div class="service-icon" style="left:468px" role="img" aria-label="Icon: jacuzzi with bubbles"></div>
  </div>

  <ul class="services">
    <li class="services__item">Real Estate Sales and Investments</li>
    <li class="services__item">Rental Management</li>
    <li class="services__item">Home Reformation Services</li>
    <li class="services__item">Landscape and Garden<br>Management</li>
    <li class="services__item">Pool and Jacuzzi Service</li>
  </ul>

  <div class="brand-mini">
    <div class="brand-mini__name">bayridgedwell48.com</div>
    <div class="brand-mini__tag">REAL ESTATE-REFORMS-HOME SERVICES</div>
  </div>
</section>

</body>
</html>
```